Womens Scarves & Accessories Homepage Design

When developing this site design please have a focus on modern, stylish design. A good example of the kind of design style the client really like can be found at www.qorvistyle.com

As fashion products are the focus here clear, appealing presentation of product images is critical.

We are after a combination of http://dev40.kqrtw.com.au/index.php/ mixed in with the brief file attached.

Some hero shot images have been attached

Target Market(s)

Consumer:
Lady 30 - 50
high disposable income
updating wardrobe
enjoys the shopping experience

Industry/Entity Type

Fashion

Requirements
Must have
• premium quality and elegant products - well packaged - boutique and elegant in style

The current logo must not be changed.

The slogan "spoil the girl within" must remain the same and use the current font displayed in http://dev40.kqrtw.com.au

```html
<!DOCTYPE html>
<html lang="en">
<head>
<meta charset="utf-8">
<title>Veloria – Spoil The Girl Within</title>
<link href="https://fonts.googleapis.com/css2?family=Open+Sans:wght@300;400;600;800&display=swap" rel="stylesheet">
<style>
:root{
  --black:#141414;
  --beige:#e5e0ca;
  --beige-light:#ebe7d4;
  --hero-bg:#f3f1ea;
  --side:#62605d;
  --side-dark:#545250;
  --tab:#d6d2c3;
  --footer:#5d5955;
  --ink:#3a3835;
  --white:#ffffff;
  --pink:#f3dbe6;
  --accent:#e08ab5;
  --gold:#e8b830;
}
*{box-sizing:border-box;margin:0;padding:0}
html,body{width:1200px;height:900px;overflow:hidden}
body{position:relative;background:var(--white);font-family:"Open Sans",Arial,sans-serif;color:var(--ink)}
.abs{position:absolute}

.topbar{left:0;top:0;width:1200px;height:55px;background:var(--black)}
.beige-band{left:0;top:55px;width:1200px;height:408px;background:var(--beige)}
.footer{left:0;top:835px;width:1200px;height:65px;background:var(--footer)}

.logo{left:258px;top:4px;width:148px;height:110px;border-radius:50%;background:var(--beige-light);border:3px solid #fff;box-shadow:0 0 0 2px #cfc9b2;display:flex;align-items:center;justify-content:center}
.logo-inner{width:128px;height:92px;border-radius:50%;background:var(--pink);border:2px solid var(--ink);display:flex;align-items:center;justify-content:center}
.logo-name{font-size:20px;font-weight:400;color:var(--ink);letter-spacing:1px}
.slogan{left:401px;top:4px;color:var(--white);font-size:22px;font-weight:400;line-height:23px;letter-spacing:-0.3px}
.slogan span{display:block;padding-left:16px}

.cart{left:764px;top:0;width:184px;height:55px;background:var(--side-dark)}
.cart-tab{left:0;top:0;width:18px;height:55px;background:#77746f;color:#ddd;font-size:10px;writing-mode:vertical-rl;transform:rotate(180deg);text-align:center;line-height:18px}
.cart-links{left:59px;top:4px;font-size:7.5px;font-weight:600;color:#ddd;white-space:nowrap;display:flex;gap:11px}
.cart-status{left:58px;top:25px;font-size:10.5px;letter-spacing:-0.2px;color:#fff;white-space:nowrap}

.nav{left:417px;top:76px;display:flex;gap:17px;font-size:13.5px;color:var(--ink);white-space:nowrap}
.nav a{color:inherit;text-decoration:none}
.search{left:789px;top:74px;width:155px;height:21px;background:#fff;border:1px solid #d8d3c0;border-radius:3px;font-size:7px;color:#aaa;padding:5px 8px}
.search svg{position:absolute;right:3px;top:2px}

.hero{left:253px;top:115px;width:510px;height:255px;background:var(--hero-bg)}
.hero-photo{left:0;top:0;width:175px;height:255px;background:linear-gradient(160deg,#d9d1c6,#7d5e55 45%,#3a2d2c)}
.hero-title{left:182px;top:24px;line-height:48px;white-space:nowrap}
.hero-title .thin{font-size:54px;font-weight:300;color:#333;letter-spacing:-1.5px;display:block}
.hero-title .bold{font-size:54px;font-weight:800;color:#111;letter-spacing:-2.5px;display:block;padding-left:68px}
.hero-copy{left:181px;top:143px;width:325px;font-size:9px;line-height:14.6px;color:#555;letter-spacing:0.15px}

.tiles{left:251px;top:370px;width:512px;height:93px;display:grid;grid-template-columns:repeat(3,1fr);gap:1px;background:#c8c3b2}
.tile{position:relative;background:linear-gradient(#8e8a82,#5c5954);color:#fff;font-size:18px;font-weight:300;padding:7px 8px;white-space:nowrap}
.tile small{position:absolute;right:6px;bottom:4px;font-size:10px;color:#e6e2d8}

.sidebar{left:764px;top:115px;width:184px;height:738px;background:var(--side);z-index:2}
.side-head{left:4px;width:180px;height:23px;background:linear-gradient(90deg,#dcd8c8,#b9b4a4);border-radius:10px 0 0 10px;font-size:13.5px;color:#444;padding:2px 10px}
.why{left:10px;top:42px;font-size:11px;color:#eee;line-height:26px;list-style:none;white-space:nowrap}
.why li{display:flex;align-items:center;gap:10px}
.why b{font-weight:600;color:#fff}
.testi{left:13px;top:172px;width:160px;font-size:8.2px;line-height:12.6px;color:#d8d5cf}
.testi p.name{color:#fff;margin:12px 0 16px}
.view-all{left:105px;top:323px;font-size:12px;color:#fff;display:flex;align-items:center;gap:6px}
.cards-row{left:40px;top:405px;display:flex;gap:20px}
.offline{left:0;top:443px;width:184px;text-align:center;color:#fff;font-size:20px;font-weight:300;line-height:26px}
.secure{left:26px;top:510px;font-size:13px;color:#fff;display:flex;align-items:center;gap:6px;white-space:nowrap}
.badge{left:24px;top:534px;width:138px;height:26px;background:#f1f0ec;border-radius:3px}
.copyright{left:0;top:720px;width:184px;height:18px;background:var(--black);color:#ddd;font-size:9px;text-align:center;line-height:18px;white-space:nowrap}

.product{top:485px;width:153px;height:330px}
.product .ptitle{height:26px;background:var(--tab);border-radius:6px 6px 0 0;font-size:13px;color:#444;padding:4px 8px;white-space:nowrap}
.product .pimg{height:231px}
.product .pdesc{height:43px;background:var(--beige);font-size:8.5px;line-height:11px;color:#555;padding:5px 7px}
.product .pbar{height:30px;background:var(--side);border-radius:0 0 6px 6px;color:#fff;display:flex;justify-content:space-between;align-items:center;padding:0 7px 0 9px}
.product .price{font-size:14px}
.product .add{font-size:12px;color:#eee}

.footer-links{left:280px;top:859px;width:430px;text-align:center;font-size:8.5px;color:#eee;line-height:11.5px;word-spacing:1px}
</style>
</head>
<body>
<div class="abs topbar"></div>
<div class="abs beige-band"></div>
<div class="abs footer"></div>

<div class="abs logo"><div class="logo-inner"><span class="logo-name">Veloria</span></div></div>
<div class="abs slogan">Spoil The<span>Girl Within</span></div>

<div class="abs cart">
  <div class="abs cart-tab">My Cart</div>
  <svg class="abs" style="left:22px;top:5px" width="34" height="44" viewBox="0 0 34 44">
    <path d="M3 12 L31 10 L28 40 L7 42 Z" fill="var(--gold)" stroke="#b58a10"/>
    <path d="M8 12 Q17 0 26 10" fill="none" stroke="#e8d070" stroke-width="2"/>
  </svg>
  <div class="abs cart-links"><span>My Wishlist</span><span>My Cart</span><span>Checkout</span></div>
  <div class="abs cart-status">Now in Your Cart 0 Items</div>
</div>

<nav class="abs nav"><a>Shop</a><a>About us</a><a>Testimonials</a><a style="margin:0 6px">FAQ</a><a>Contact us</a></nav>
<div class="abs search">Search now
  <svg width="15" height="15" viewBox="0 0 15 15"><circle cx="6" cy="6" r="4.5" fill="none" stroke="var(--accent)" stroke-width="2"/><path d="M9.5 9.5 L13 13" stroke="var(--accent)" stroke-width="2.5"/></svg>
</div>

<section class="abs hero">
  <div class="abs hero-photo" role="img" aria-label="Photo of two women wearing colourful scarves and shawls"></div>
  <h1 class="abs hero-title"><span class="thin">Wraps</span><span class="bold">&amp;Shawls</span></h1>
  <p class="abs hero-copy">simply dummy text of the printing and typesetting industry. Lorem Ipsum has been the industry's standard dummy text ever since<br><br>the 1500s,text of the printing and typesetting industry simply dummy text of the printing and typesetting industry.<br>Lorem Ipsum has been the industry's standard dummy text</p>
</section>

<div class="abs tiles">
  <div class="tile">Scarves<small>More info.</small></div>
  <div class="tile">Wraps &amp; shawls<small>More info.</small></div>
  <div class="tile">Costume Jewelry<small>More info.</small></div>
  <div class="tile">Accessories<small>More info.</small></div>
  <div class="tile">Gifts<small>More info.</small></div>
  <div class="tile">Specials<small>More info.</small></div>
</div>

<aside class="abs sidebar">
  <div class="abs side-head" style="top:7px">Why Veloria?</div>
  <ul class="abs why">
    <li><svg width="10" height="10"><circle cx="5" cy="5" r="4" fill="none" stroke="#eee"/><path d="M4 3 L7 5 L4 7Z" fill="#eee"/></svg><span><b>90</b> Days Return Policy</span></li>
    <li><svg width="10" height="10"><circle cx="5" cy="5" r="4" fill="none" stroke="#eee"/><path d="M4 3 L7 5 L4 7Z" fill="#eee"/></svg><span><b>Free</b> Shipping Both Ways</span></li>
    <li><svg width="10" height="10"><circle cx="5" cy="5" r="4" fill="none" stroke="#eee"/><path d="M4 3 L7 5 L4 7Z" fill="#eee"/></svg><span><b>Loyalty</b> Program</span></li>
  </ul>
  <div class="abs side-head" style="top:140px">Testimonials</div>
  <div class="abs testi">
    <p>Lorem ipsum dolor sit amet, consect-etur adipiscing elit. Donec euismod arcu a mi fermentum varius.</p>
    <p class="name">Jane Smith - Fakeville</p>
    <p>Lorem ipsum dolor sit amet, consect-etur adipiscing elit. Donec euismod arcu a mi fermentum varius.</p>
    <p class="name">Jane Smith - Fakeville</p>
  </div>
  <div class="abs view-all">VIEW ALL <svg width="14" height="14"><circle cx="7" cy="7" r="6" fill="none" stroke="#fff" stroke-width="1.5"/><path d="M5.5 4 L9 7 L5.5 10" fill="none" stroke="#fff" stroke-width="1.5"/></svg></div>
  <div class="abs side-head" style="top:370px">Payment Methods</div>
  <div class="abs cards-row">
    <svg width="40" height="26"><rect x="1" y="1" width="38" height="24" rx="2" fill="#f4f2ec" stroke="#d9a640"/></svg>
    <svg width="46" height="32"><rect x="2" y="4" width="36" height="22" rx="2" fill="#8fc3e8"/><rect x="10" y="10" width="34" height="20" rx="2" fill="#3c9b4a"/></svg>
  </div>
  <div class="abs offline">Offline Payments<br><span style="font-weight:400">ACCEPTED</span></div>
  <div class="abs secure"><svg width="22" height="14"><rect width="22" height="14" rx="2" fill="var(--gold)"/></svg>Secure Shopping</div>
  <div class="abs badge"></div>
  <div class="abs copyright">© 2011 Veloria. All Rights reserved</div>
</aside>

<article class="abs product" style="left:253px">
  <div class="ptitle">Modern Scarf</div>
  <div class="pimg" role="img" aria-label="Product photo of a woman wearing a pink checked scarf" style="background:linear-gradient(170deg,#8a6a55,#3b3230 55%,#b0306e)"></div>
  <div class="pdesc">simply dummy text of the printi-ng and typesetting industry. Lorem Ipsum</div>
  <div class="pbar"><span class="price">$299</span><span class="add">Add to Cart</span></div>
</article>
<article class="abs product" style="left:423px">
  <div class="ptitle">Wraps &amp; Shawls</div>
  <div class="pimg" role="img" aria-label="Product photo of a woman in a dark grey belted wrap coat" style="background:linear-gradient(#ebebef,#d0d0d5 30%,#4a4a4c 60%,#d8d8dc)"></div>
  <div class="pdesc">simply dummy text of the printi-ng and typesetting industry. Lorem Ipsum</div>
  <div class="pbar"><span class="price">$299</span><span class="add">Add to Cart</span></div>
</article>
<article class="abs product" style="left:594px">
  <div class="ptitle">Costume Jewelry</div>
  <div class="pimg" role="img" aria-label="Product photo of a gold and pink costume necklace set on a black display" style="background:radial-gradient(circle at 45% 40%,#a06a3a,#3a1a20 45%,#0b0b0d 80%)"></div>
  <div class="pdesc">simply dummy text of the printi-ng and typesetting industry. Lorem Ipsum</div>
  <div class="pbar"><span class="price">$299</span><span class="add">Add to Cart</span></div>
</article>

<div class="abs footer-links">BEST SELLERS &nbsp;| &nbsp;SCARVES &nbsp;| &nbsp;WRAPS &amp; SHAWLS &nbsp;| &nbsp;ACCESSORIES &nbsp;| &nbsp;GIFTS &nbsp;| &nbsp;PECIALS &nbsp;| &nbsp;ABOUT US &nbsp;| &nbsp;TESTIMONIALS &nbsp;&nbsp;| &nbsp;FAQ &nbsp;| &nbsp;CONTACT US</div>
</body>
</html>
```